Energy cost saving website (job description rewritten!)

Job Type: WordPress design
Task Outline: Create a WordPress design
Task Description:
We are new business (Germany) in the market of saving costs by power-saving (name: 'wir-falten-eure-Wolkenbögen.de'). This is reached by changing the supplier, the use of LED bulbs, energy saving washing machines, stoves, microwaves, hairdryers, vacuum cleaners and the like - where all of these be selled or affiliated through the website maybe you will create for us.
Design parameters:
We want a serious design that embodies a feeling of honesty, competence and capability.
Visitors should particularly see that this site saves them money!
The home page mainly should act as a selector of possibilities saving money by power-saving, usage of LED bulbs and large energy saving household devices (washing machines, etc.)
Updates
Hello designers,
browsing through the PixelHarbors files of portfolios I found one header graphics which excites me. Please find it here: http://www.pixelharbor-example.net/design/482716/wordpress-design-by-tarek-olumide . Note: it is NOT the picture but the shadowing. So if you consider this in your concepts would be another 'nice-to-have'.
Thanks.
Target Market(s)
People looking out for saving money by power-saving.
Industry/Entity Type
Business
Requirements
Must have
- Look and feel of 'this site saves me money'!
Nice to have
- We love 3D effects, but its not a must have. We also like cartoons, but feel free to develop your own concept, please. An appropriate backgrond picture would be nice.
Should not have
- Some kind of these exaggerated smiling or handshaking photos. That bathetic symbols like money bills or coins stacks.

```html
<!DOCTYPE html>
<html lang="de">
<head>
<meta charset="utf-8">
<title>Wir falten eure Wolkenbögen</title>
<link href="https://fonts.googleapis.com/css2?family=Ubuntu:wght@300;400;500;700&family=Quicksand:wght@500;600&family=Noto+Serif:wght@700&display=swap" rel="stylesheet">
<style>
:root{
  --page-bg:#efefef;
  --sheet:#f8f8f8;
  --green-dark:#3f6e0c;
  --green:#7db522;
  --green-light:#a3d13c;
  --blue-title:#3d8fd1;
  --blue-tag:#5c7fc4;
  --blue-bullet:#2f77b8;
  --card-top:#d3e3f1;
  --card-body:#dce8f2;
  --text-grey:#8a8a8a;
  --text-dark:#444;
}
*{margin:0;padding:0;box-sizing:border-box}
html,body{width:1200px;height:1011px;overflow:hidden}
body{background:var(--page-bg);font-family:'Ubuntu',sans-serif;position:relative}
.sheet{position:absolute;left:180px;top:43px;width:840px;height:934px;background:var(--sheet);border-radius:6px;box-shadow:0 0 6px rgba(0,0,0,.06)}
.brand{position:absolute;left:231px;top:58px;font-family:'Ubuntu',sans-serif;font-weight:500;color:var(--green-dark);font-size:30px;line-height:31px;letter-spacing:-.3px}
.tagline{position:absolute;left:231px;top:118px;font-size:11px;color:var(--blue-tag);letter-spacing:.8px}
.social{position:absolute;left:852px;top:116px;display:flex;gap:14px}
.social span{width:14px;height:14px;border-radius:50%;background:#b4b4b4;display:block}
.hero{position:absolute;left:228px;top:155px;width:744px;height:315px;background:radial-gradient(ellipse at 45% 40%,#c8e86a 0%,#8fc734 40%,#5e9a1c 100%);overflow:hidden}
.hero-visual{position:absolute;left:0;bottom:0;width:744px;height:315px;background:linear-gradient(180deg,transparent 60%,rgba(60,120,20,.55) 85%,#3e7a14 100%)}
.hero-visual .lamp{position:absolute;border-radius:50%;background:radial-gradient(circle at 55% 40%,#f4f4f4 0%,#c9c9c9 35%,#777 70%,#9a9a9a 100%)}
.hero h1{position:absolute;left:21px;top:34px;font-weight:300;color:#fff;font-size:36px;line-height:36px;letter-spacing:.3px}
.hero h1 b{font-weight:700}
.hero p{position:absolute;left:22px;top:115px;width:320px;font-size:15px;line-height:20.6px;color:#fff}
.hero-shadow{position:absolute;left:200px;top:470px;width:800px;height:26px;background:radial-gradient(ellipse at 50% 0%,rgba(0,0,0,.35) 0%,rgba(0,0,0,.08) 45%,transparent 70%)}
.arrow{position:absolute;top:314px}
.card{position:absolute;top:540px;width:221px;height:351px;background:#fff;box-shadow:0 2px 5px rgba(0,0,0,.25);padding:3px}
.card-inner{position:relative;height:100%;background:linear-gradient(180deg,#f6f9fb 0%,var(--card-body) 100%)}
.card-head{height:55px;background:linear-gradient(180deg,#e4eef7,var(--card-top));display:flex;align-items:center;padding-left:13px;border-bottom:1px solid #c5d7e8}
.card-icon{width:43px;height:43px;border-radius:7px;background:linear-gradient(180deg,#4c9be0,#1c5da6);margin-right:19px;flex:none;display:flex;align-items:center;justify-content:center}
.card-title{font-family:'Quicksand',sans-serif;font-weight:600;font-size:14px;color:var(--blue-title);letter-spacing:.3px}
.card-body{padding:16px 20px 0 23px;font-size:9.6px;line-height:15.4px;color:var(--text-grey)}
.q-list{list-style:none;padding-left:0}
.q-list li{position:relative;padding:0 0 4px 15px;margin-bottom:6px;border-bottom:1px solid #d9dfe4;line-height:12px}
.q-list li:last-child{border:none}
.q-list li::before,.dev-list li::before{content:"";position:absolute;left:0;top:4px;width:4px;height:4px;border-radius:50%;background:var(--blue-bullet)}
.cta-note{text-align:center;font-size:10px;color:#5a3a3a;margin-top:-4px}
.card-body.plain{padding-left:20px;line-height:15.5px}
.card-body.dense{line-height:12.5px;padding-left:23px}
.dev-list{list-style:none;margin-top:22px;padding-left:3px;color:var(--text-dark);font-size:10px}
.dev-list li{position:relative;padding-left:11px;line-height:17.2px}
.dev-list li::before{top:7px}
.card-btn{position:absolute;left:0;top:288px;width:100%;height:36px;background:linear-gradient(180deg,var(--green-light),#6ea81a);border-bottom:1px solid #5a8f12;display:flex;align-items:center;justify-content:center;font-family:'Noto Serif',serif;font-weight:700;font-size:12px;color:#fff;text-decoration:underline}
.footer-rule{position:absolute;left:190px;top:920px;width:820px;height:2px;background:linear-gradient(90deg,transparent,#d8d8d8 20%,#d8d8d8 80%,transparent)}
.footer-nav{position:absolute;left:224px;top:941px;display:flex;gap:12px;font-size:10.5px;color:#555}
.copyright{position:absolute;right:211px;top:941px;font-size:10.5px;color:#555}
</style>
</head>
<body>
<div class="sheet"></div>

<div class="brand">Wir falten eure<br>Wolkenbögen</div>
<div class="tagline">Jedes Jahr neu!</div>
<div class="social" aria-label="Social links"><span></span><span></span><span></span><span></span></div>

<svg class="arrow" style="left:203px" width="14" height="16" viewBox="0 0 14 16"><path d="M11 2 L4 8 L11 14" fill="none" stroke="#3f6e0c" stroke-width="3"/></svg>
<svg class="arrow" style="left:984px" width="14" height="16" viewBox="0 0 14 16"><path d="M3 2 L10 8 L3 14" fill="none" stroke="#3f6e0c" stroke-width="3"/></svg>

<div class="hero">
  <div class="hero-visual" role="img" aria-label="LED spotlight bulbs lying on green grass">
    <span class="lamp" style="left:482px;top:110px;width:240px;height:205px"></span>
    <span class="lamp" style="left:100px;top:215px;width:85px;height:85px"></span>
    <span class="lamp" style="left:300px;top:215px;width:85px;height:85px"></span>
  </div>
  <h1>start saving <b>enegry</b><br>and <b>money</b> today</h1>
  <p>Lorem Ipsum est simplement du faux texte employé dans la composition et la mise en page avant impression.</p>
</div>
<div class="hero-shadow"></div>

<section class="card" style="left:228px">
  <div class="card-inner">
    <div class="card-head">
      <div class="card-icon"><svg width="22" height="26" viewBox="0 0 22 26"><rect x="1" y="1" width="20" height="24" rx="2" fill="#fff"/><path d="M5 9h12M5 13h12M5 17h8" stroke="#7a9cc0" stroke-width="1.5"/></svg></div>
      <div class="card-title">Anbieterwechsel</div>
    </div>
    <div class="card-body">
      <ul class="q-list">
        <li>Stromkosten senken durch Anbieter-wechsel zu kompliziert?</li>
        <li>Anbieterwechsel zu viel Arbeit?</li>
        <li>Anbieterwechsel hat einen schlech-ten Ruf?</li>
        <li>Angebote zur Stromkostensenkung zu verwirrend?</li>
        <li>AGBs der Stromanbieter undurch-schaubar?</li>
        <li>Jedes Jahr neu entscheiden und kümmern?</li>
      </ul>
      <div class="cta-note">WIR MACHEN DAS</div>
    </div>
    <a class="card-btn">zum Rundum-sorglos-Paket</a>
  </div>
</section>

<section class="card" style="left:489px">
  <div class="card-inner">
    <div class="card-head">
      <div class="card-icon"><svg width="24" height="24" viewBox="0 0 24 24"><circle cx="14" cy="10" r="7" fill="none" stroke="#fff" stroke-width="2"/><path d="M9 15 L3 21" stroke="#fff" stroke-width="3"/></svg></div>
      <div class="card-title">LED-Leuchtmittel</div>
    </div>
    <div class="card-body plain">Sie sind die Leuchtmittel der Zukunft und so wollen wir auch an dieser Stelle mit gutem Beispiel voran gehen, diese neue TEchnik vorstellen, Ängste und Vorurteile abbauen und LEDs vorstellen und empfehlen.<br>Noch sind sie relativ teuer, sie spielen jedoch ihre Kosten meist in weniger als 2 Jahren wieder herin.<br>Selbstverständlich finden Sie hier auch einen Amortisationsrechner, der Ihnen das genau ausrechnet - Leuchtmittel für Leuchtmittel.</div>
    <a class="card-btn">zu den LEDs</a>
  </div>
</section>

<section class="card" style="left:749px">
  <div class="card-inner">
    <div class="card-head">
      <div class="card-icon" style="margin-right:9px"><svg width="24" height="26" viewBox="0 0 24 26"><rect x="1" y="1" width="22" height="24" rx="2" fill="#e8eef4"/><circle cx="12" cy="15" r="6" fill="none" stroke="#4c86c0" stroke-width="2"/></svg></div>
      <div class="card-title">Haushaltsgroßgeräte</div>
    </div>
    <div class="card-body dense">Hier lässt sich eine Menge Strom und damit natürlich eben auch Kosten sparen. wir-falten-eure-Wolkenbögen.de stellt Ihnen an dieser Stelle daher die sparsamsten Modelle vor:
      <ul class="dev-list">
        <li>Waschmaschinen</li>
        <li>Waschtrockner</li>
        <li>Wäschetrockner</li>
        <li>Weinkühlschränke</li>
        <li>Kühlschränke</li>
        <li>Herde/Backöfen</li>
        <li>Geschirrspüler</li>
      </ul>
    </div>
    <a class="card-btn">Zum Energieverbrauch Vergleich</a>
  </div>
</section>

<div class="footer-rule"></div>
<nav class="footer-nav"><span>Home</span><span>Tips</span><span>Product</span><span>Services</span><span>About Us</span></nav>
<div class="copyright">ALDERWICK GROUP Copyright © 2012 All Rights Reserved.</div>
</body>
</html>
```